Business Card for a Life Coaching Company

BRAVOPEAK is a Life Coaching company that was initiated to support people who want to transform thier life or ana aspect of it.
our slogan is : "Dream. Believe. Succeed"
our logo is uploaded.
The name of the company implies that leadership, strength and wisdom required to change your life.
We want an attractive business card that would give an impression of reliability, support and change. so we really want it unique. Here are some examples of unique cards:

http://www.cardcraftvault.example/2009/05/100-really-creative-business-cards/

BravoPeak is a life coaching organization focusing on individual transformation through the application of relevant and timeless principles of success.  BravoPeak believes that real, sustainable life transformations are brought about by tuning into the timeless wisdom we each carry in our hearts while boldy acting in the direction of our dreams.

Contacts on the card:
Address: 7 Tarek Nour El Dine Heliopolis Cairo Egypt
Tel: +202 24 71 38 52
Fax: +202 24 71 38 17
Mobile: +2 012 684 2097 (Dalia Soliman)
+2 0199915815 (Tariq Bhatti)

By the way, our temporary website is http://www.bravopeak.example

We have attached an .eps file with various configurations of our logo.

```html
<!DOCTYPE html>
<html lang="en">
<head>
<meta charset="utf-8">
<title>BravoPeak Business Card</title>
<link rel="stylesheet" href="https://fonts.googleapis.com/css2?family=Carlito:wght@400;700&display=swap">
<style>
  :root {
    --brand-orange: #f05a28;
    --brand-orange-soft: #f58a5f;
    --ink-dark: #333333;
    --ink-mid: #555555;
    --logo-grey: #8a8a8a;
    --card-white: #ffffff;
    --page-bg: #ffffff;
  }
  * { margin: 0; padding: 0; box-sizing: border-box; }
  html, body {
    width: 960px;
    height: 1200px;
    overflow: hidden;
    background: var(--page-bg);
    font-family: "Carlito", "Calibri", sans-serif;
  }
  .canvas { position: relative; width: 960px; height: 1200px; }

  .card {
    position: absolute;
    left: 111px;
    width: 741px;
    height: 451px;
    background: var(--card-white);
    overflow: hidden;
    box-shadow: 0 6px 14px rgba(0, 0, 0, 0.28);
  }
  .card-front { top: 111px; }
  .card-back { top: 639px; }
  .card-art { position: absolute; inset: 0; width: 100%; height: 100%; }
  .card-art .brand-fill { fill: var(--brand-orange); }

  .illustration-area {
    position: absolute;
    top: 0;
    right: 0;
    width: 236px;
    height: 451px;
    background: linear-gradient(160deg, var(--brand-orange-soft), var(--brand-orange));
  }

  .slogan {
    position: absolute;
    left: 60px;
    top: 222px;
    font-size: 35px;
    font-weight: 700;
    color: var(--ink-mid);
    white-space: nowrap;
  }
  .slogan .dot { color: var(--brand-orange); }

  .logo {
    position: absolute;
    left: 30px;
    top: 52px;
    display: flex;
    align-items: center;
    gap: 12px;
  }
  .logo-mark {
    width: 26px;
    height: 26px;
    background: var(--brand-orange);
  }
  .logo-name {
    font-size: 40px;
    font-weight: 400;
    color: var(--logo-grey);
    letter-spacing: 1px;
  }

  .contact-person {
    position: absolute;
    right: 22px;
    top: 28px;
    text-align: right;
  }
  .person-name {
    font-size: 33px;
    font-weight: 700;
    color: var(--brand-orange);
    line-height: 1.2;
  }
  .person-role {
    font-size: 24px;
    font-weight: 700;
    color: var(--ink-dark);
    line-height: 1.3;
  }
  .person-mobile {
    font-size: 22px;
    font-weight: 700;
    color: var(--ink-dark);
    line-height: 1.3;
  }

  .company-details {
    position: absolute;
    left: 28px;
    top: 322px;
    font-size: 22px;
    font-weight: 700;
    font-style: normal;
    color: var(--ink-dark);
    line-height: 31px;
  }
  .company-details .web-link { color: var(--brand-orange); }
</style>
</head>
<body>
<main class="canvas">

  <section class="card card-front" aria-label="Business card front">
    <svg class="card-art" viewBox="0 0 741 451" aria-hidden="true">
      <path class="brand-fill" d="M0,155 C30,330 250,440 592,451 L0,451 Z"/>
    </svg>
    <div class="illustration-area" role="img" aria-label="Large orange brand illustration"></div>
    <p class="slogan">Dream <span class="dot">.</span> Believe <span class="dot">.</span> Succeed</p>
  </section>

  <section class="card card-back" aria-label="Business card back">
    <svg class="card-art" viewBox="0 0 741 451" aria-hidden="true">
      <path class="brand-fill" d="M741,160 C705,330 565,430 401,451 L741,451 Z"/>
    </svg>

    <div class="logo">
      <span class="logo-mark" aria-hidden="true"></span>
      <span class="logo-name">BRAVOPEAK</span>
    </div>

    <div class="contact-person">
      <p class="person-name">Dalia Soliman</p>
      <p class="person-role">designation</p>
      <p class="person-mobile">M: +2 012 684 2097</p>
    </div>

    <address class="company-details">
      <p>7 Tarek Nour El Dine Heliopolis Cairo Egypt</p>
      <p>T: +202 24 71 38 52 | F: +202 24 71 38 17</p>
      <p>W: <span class="web-link">www.bravopeak.example</span></p>
    </address>
  </section>

</main>
</body>
</html>
```